Need UI design for an iOS app game with most of the layout planned

The name of the game is "QUADRIX".

The goal of the game is to find a way to manipulate four numbers so that the end result is 24. Addition, subtraction, multiplication and division may be used and each number can only be used once.

The list of items we need is:

1. launch image, app icon, UI design of all scenes (10-12 scenes) of the app.
2. App background image should support screen size of both 640x1136.
3. Files are preferred to be in (.eps) format so that resolution can be adjusted later. But other file formats are welcome as long as resolution is high enough.
4. Icons, buttons, background image etc. should have their own file so that later they can be moved around in case design is changed.

The detailed requirement is in the attached file. The actual layout can vary if it can help achieve better result. We also attached several screenshots from iOS game "Glimtor". You can use that as your reference.

```html
<!DOCTYPE html>
<html lang="en">
<head>
<meta charset="utf-8">
<title>QUADRIX – Main Menu</title>
<link rel="stylesheet" href="https://fonts.googleapis.com/css2?family=Fredoka:wght@600&family=Open+Sans:wght@600;800&display=swap">
<style>
  :root {
    --page-bg: #e9e6e1;
    --screen-blue-light: #5b9cec;
    --screen-blue-dark: #2f5fc0;
    --status-text: #0b1a33;
    --gear-bg: #1d1f24;
    --help-yellow: #f5b21c;
    --help-yellow-dark: #e0960a;
    --single-yellow: #f7d418;
    --single-yellow-dark: #f2a51a;
    --multi-red: #e8161a;
    --multi-red-dark: #b90d10;
    --button-text: #ffffff;
    --logo-orange: #f7a21b;
    --logo-dot: #e8161a;
  }
  * { box-sizing: border-box; margin: 0; padding: 0; }
  html, body { width: 1200px; height: 900px; overflow: hidden; }
  body {
    background: var(--page-bg);
    position: relative;
    font-family: "Open Sans", sans-serif;
  }
  .app-screen {
    position: absolute;
    left: 100px; top: 168px;
    width: 1000px; height: 563px;
    border-radius: 6px;
    overflow: hidden;
    background: radial-gradient(ellipse at 58% 40%, var(--screen-blue-light) 0%, var(--screen-blue-dark) 100%);
  }
  .status-bar {
    position: absolute; left: 0; top: 0; width: 100%; height: 22px;
    display: flex; align-items: center; justify-content: space-between;
    padding: 0 10px;
    font-size: 13px; font-weight: 600; color: var(--status-text);
  }
  .status-bar .signal { display: flex; gap: 3px; align-items: center; }
  .status-bar .signal span { width: 6px; height: 6px; border-radius: 50%; background: var(--status-text); }
  .status-bar .signal span.empty { background: none; border: 1px solid var(--status-text); }
  .status-bar .battery { display: flex; align-items: center; gap: 5px; }
  .battery-icon { width: 24px; height: 11px; border: 1px solid var(--status-text); border-radius: 2px; padding: 1px; }
  .battery-icon i { display: block; width: 100%; height: 100%; background: var(--status-text); }
  .settings-button {
    position: absolute; left: 22px; top: 36px;
    width: 44px; height: 44px; border-radius: 50%;
    background: var(--gear-bg);
    display: flex; align-items: center; justify-content: center;
    box-shadow: 0 2px 4px rgba(0,0,0,.35);
  }
  .help-button {
    position: absolute; right: 36px; top: 150px;
    width: 46px; height: 46px; border-radius: 50%;
    background: radial-gradient(circle at 50% 35%, var(--help-yellow), var(--help-yellow-dark));
    color: #fff; font: 800 24px/46px "Open Sans", sans-serif; text-align: center;
    box-shadow: 0 2px 4px rgba(0,0,0,.3);
  }
  .game-title {
    position: absolute; left: 0; top: 110px; width: 100%;
    display: flex; justify-content: center; align-items: center; gap: 14px;
  }
  .game-title .title-dot { width: 26px; height: 26px; border-radius: 50%; background: var(--logo-dot); }
  .game-title h1 {
    font-family: "Fredoka", sans-serif; font-weight: 600;
    font-size: 84px; line-height: 1; color: var(--logo-orange);
  }
  .menu { position: absolute; left: 0; top: 268px; width: 100%; }
  .menu-button {
    position: absolute; height: 74px; width: 560px;
    display: flex; align-items: center;
    border-radius: 6px; overflow: hidden;
    box-shadow: 0 4px 8px rgba(0,0,0,.3);
    color: var(--button-text);
    font-weight: 800; font-size: 34px;
    text-shadow: 0 2px 2px rgba(0,0,0,.35);
  }
  .menu-button .icon-cell { width: 82px; height: 100%; display: flex; align-items: center; justify-content: center; }
  .menu-button .label { flex: 1; text-align: center; padding-right: 40px; }
  .menu-button--single { left: 240px; top: 0; background: linear-gradient(90deg, var(--single-yellow-dark) 0%, var(--single-yellow) 40%); }
  .menu-button--single .icon-cell { background: var(--single-yellow-dark); }
  .menu-button--multi { left: 200px; top: 100px; background: var(--multi-red); }
  .menu-button--multi .icon-cell { background: var(--multi-red-dark); }
</style>
</head>
<body>
  <main class="app-screen">
    <div class="status-bar">
      <div class="signal"><span></span><span></span><span></span><span class="empty"></span><span class="empty"></span></div>
      <div class="clock">4:21 PM</div>
      <div class="battery">100% <div class="battery-icon"><i></i></div></div>
    </div>

    <div class="settings-button" aria-label="Settings">
      <svg width="26" height="26" viewBox="0 0 24 24" fill="#fff">
        <path d="M10.5 1h3l.5 3 2 .9 2.5-1.8 2.1 2.1-1.8 2.5.9 2 3 .5v3l-3 .5-.9 2 1.8 2.5-2.1 2.1-2.5-1.8-2 .9-.5 3h-3l-.5-3-2-.9-2.5 1.8-2.1-2.1 1.8-2.5-.9-2-3-.5v-3l3-.5.9-2-1.8-2.5 2.1-2.1 2.5 1.8 2-.9z"/>
        <circle cx="12" cy="12" r="3.6" fill="#1d1f24"/>
      </svg>
    </div>

    <div class="help-button" aria-label="Help">?</div>

    <header class="game-title">
      <span class="title-dot"></span>
      <h1>QUADRIX</h1>
    </header>

    <nav class="menu">
      <div class="menu-button menu-button--single">
        <span class="icon-cell">
          <svg width="38" height="38" viewBox="0 0 24 24" fill="#fff"><circle cx="12" cy="8" r="5"/><path d="M2 23c0-6 4.5-9 10-9s10 3 10 9z"/></svg>
        </span>
        <span class="label">Single Player</span>
      </div>
      <div class="menu-button menu-button--multi">
        <span class="icon-cell">
          <svg width="42" height="38" viewBox="0 0 28 24" fill="#fff"><circle cx="18" cy="7" r="4.5"/><path d="M9 22c0-5.5 4-8 9-8s9 2.5 9 8z"/><circle cx="9" cy="9" r="4" opacity=".8"/><path d="M1 22c0-5 3.5-7.5 8-7.5 1.5 0 2.8.3 3.8.8-2 1.6-3 4-3 6.7z" opacity=".8"/></svg>
        </span>
        <span class="label">MultiPlayer</span>
      </div>
    </nav>
  </main>
</body>
</html>
```